Boutique Shoe Bag Race wear Business Card Design

We are a new luxury shoe bag, jewellery and race wear store stocking local and international designers. Located in the fashion precinct of beautiful Calloway Cove famous in Sydney Australia. Stocking French jewellery and shoes such as Renaud valmiers plus Australian made. Looking at quality and service and looking after the locals and tourists.
Ideas: White background, Black writing in bold engravers, logo in middle of Marlow and Boutique a gold horseshoe (facing upright so the curve is at the bottom) with a black stiletto inside. French clover silver and black border (not irish clover the French lattice type look)
Updates

Marlow Atelier

I open 8/4 so require business card design ASAP.

Please place gold horseshoe facing upwards with the black stiletto inside.

Bold engravers writing for business name.

I will have my phone number tomorrow to update.

Border in similar/same style as attached picture with black/silver clover French design.

Thank you. Tessa                                   

Industry/Entity Type

Fashion

Contact Information for Business Card

Marlow Atelier
Boutique Owner Tessa Wrenfield
41B Parrin Lane
Calloway Cove NSW 2093 Australia
0471239046
02 **** *TBA
info@marlowatelier.com.au
Lumora.com/MarlowAtelier
www.marlowatelier.com.au

Font styles to use
Other font styles liked:
• Bold Engravers

Requirements
Must have
• Info on one side including business name and logo with black stiletto and gold horse shoe. reverse side with French clover border and Larger name Marlow Atelier with logo in centre.
Should not have
• irish clover
French script
horseshoe upside down

```html
<!DOCTYPE html>
<html lang="en">
<head>
<meta charset="utf-8">
<title>Marlow Atelier – Business Card</title>
<link rel="stylesheet" href="https://fonts.googleapis.com/css2?family=Cinzel:wght@400;600;700&display=swap">
<style>
  :root {
    --backdrop: #ece9e3;
    --card: #ffffff;
    --ink: #1a1a1a;
    --gold: #c99a1c;
    --gold-light: #e4bb45;
    --gold-deep: #a87c0e;
    --clover-tint: #dcebd6;
    --clover-soft: #eef5ea;
    --shadow: rgba(0, 0, 0, 0.18);
  }
  * { box-sizing: border-box; margin: 0; padding: 0; }
  html, body {
    width: 1200px;
    height: 900px;
    overflow: hidden;
    background: var(--backdrop);
    font-family: "Cinzel", serif;
    color: var(--ink);
  }
  .canvas {
    position: relative;
    width: 1200px;
    height: 900px;
    display: flex;
    align-items: center;
    justify-content: center;
    gap: 60px;
  }
  .card {
    position: relative;
    width: 525px;
    height: 300px;
    background: var(--card);
    box-shadow: 0 10px 28px var(--shadow);
    overflow: hidden;
  }

  /* Reverse side: clover border + centred name */
  .clover-border {
    position: absolute;
    inset: 0;
    background:
      radial-gradient(ellipse 62% 58% at 50% 52%, var(--card) 45%, var(--clover-soft) 72%, var(--clover-tint) 100%);
  }
  .brand-centre {
    position: absolute;
    inset: 0;
    display: flex;
    flex-direction: column;
    align-items: center;
    justify-content: center;
    gap: 14px;
  }
  .brand-dot {
    width: 46px;
    height: 46px;
    border-radius: 50%;
    background: var(--gold);
  }
  .brand-name {
    font-weight: 700;
    font-size: 22px;
    letter-spacing: 0.06em;
    text-transform: uppercase;
    color: var(--ink);
  }

  /* Front side: contact details */
  .title-band {
    position: absolute;
    left: 0;
    right: 0;
    top: 34px;
    height: 28px;
    background: linear-gradient(90deg, var(--gold-deep), var(--gold) 40%, var(--gold-light));
  }
  .band-mark {
    position: absolute;
    left: 18px;
    top: 20px;
    height: 56px;
    padding: 0 12px;
    background: var(--card);
    display: flex;
    align-items: center;
    gap: 8px;
  }
  .band-mark .brand-dot {
    width: 26px;
    height: 26px;
  }
  .band-mark .brand-name {
    font-size: 11px;
    font-weight: 700;
    color: var(--gold-deep);
  }
  .owner-line {
    position: absolute;
    right: 22px;
    top: 34px;
    height: 28px;
    display: flex;
    align-items: center;
    gap: 8px;
    color: #fff;
    text-transform: uppercase;
  }
  .owner-role {
    font-size: 8px;
    font-weight: 600;
    letter-spacing: 0.08em;
  }
  .owner-name {
    font-size: 15px;
    font-weight: 600;
    letter-spacing: 0.04em;
  }
  .address-block {
    position: absolute;
    left: 0;
    right: 0;
    top: 128px;
    text-align: center;
    font-style: normal;
    font-size: 11px;
    font-weight: 700;
    line-height: 1.45;
    letter-spacing: 0.05em;
    text-transform: uppercase;
  }
  .footer-link {
    position: absolute;
    bottom: 22px;
    font-size: 7px;
    font-weight: 600;
    letter-spacing: 0.06em;
    color: var(--gold);
    text-transform: uppercase;
    white-space: nowrap;
  }
  .footer-link.social { left: 36px; }
  .footer-link.web { right: 36px; }
</style>
</head>
<body>
<main class="canvas">
  <section class="card card-reverse">
    <div class="clover-border" role="img" aria-label="Soft green and silver French clover lattice border fading toward the centre"></div>
    <div class="brand-centre">
      <span class="brand-dot"></span>
      <span class="brand-name">Marlow Atelier</span>
    </div>
  </section>

  <section class="card card-front">
    <div class="title-band"></div>
    <div class="band-mark">
      <span class="brand-dot"></span>
      <span class="brand-name">Marlow Atelier</span>
    </div>
    <div class="owner-line">
      <span class="owner-role">Boutique Owner</span>
      <span class="owner-name">Tessa Wrenfield</span>
    </div>
    <address class="address-block">
      41B Parrin Lane Calloway Cove<br>
      NSW 2093 Australia<br>
      0471239046 02 **** *TBA<br>
      info@marlowatelier.com.au
    </address>
    <span class="footer-link social">Lumora.com/MarlowAtelier</span>
    <span class="footer-link web">www.marlowatelier.com.au</span>
  </section>
</main>
</body>
</html>
```